Classic Personal Business Card in Regatta Dunmore Hale Style (Horizontal - Raised Ink)

If you ever seen a Dunmore Hale Regatta shirt, you will know that the signature of that shirt is small monogrammed icon on the left pocket. I envision my personal business card using some of these elements. I am in the oil exploration industry, which is very conservative and I want a card that looks great but still reflects that classic conservatism. I specifically do land management work, which means I determine who owns mineral rights, I lease those rights for larger companies to then drill for crude oil and natural gas

1. I have designed a small logo (which definitely could use some help) that I would like to be pretty small, centered in the middle of the card, and near the top of the card (color - navy blue or similar) Please feel free to make this logo infinitely better. However, I am not looking for anything abstract/

2. I want my name and designation (Marcus J. Thornbury, RPL) centered in the middle of the card. As far as font, I'm looking for a classic, strong (almost masculine) cursive font (I realize masculine + cursive is a little oxymoronic) and I would like it to the color to be Gold.

3. I would like my name (see above) to sit on top of a thin, centered navy blue (or similar) line as if it were almost a signature on a line. I want the lower-case letters that normally would dip below the line (which is y and p in my case) to do the same. I'll attach an example to help illustrate what I mean.

4. The rest of the card is my contact information. Because I am shoot for a more centered and balance look, I would like the placement of my contact information to also be centered and balance. Font should be a very classic, professional font. My first inclination is to use black for the color but I'm open to other suggestions.

Contact information:

Phone: (XXX) XXX-XXXX
Email: xxxxxxx@mailbox-example.net

Important Note: My hope is to have these printed with Raised Ink on High Quality High Quality Card Stock so it must conform to this Necessity.

Project Deadline Extended Reason: I am having major internet trouble. So I am not able to look at the submissions and provide feedback in a timely fashion. Also, it is difficult to access the site from just my phone. Added Saturday, November 22, 2014

Target Market(s)

US Oil Executives

Industry/Entity Type

Conservative

Contact Information for Business Card

I've posted a new logo that needs some clean up and a new idea for the top and bottom border of the card. I would like the logo to be centered in the top border with a white barrier on either side between the logo and the border. I've also posted color codes below.

Thanks

Requirements
Must have
• Color Codes:
• Blue: R - 0 G - 0 B - 102
• Gold R - 102 G - 102 B - 0

```html
<!DOCTYPE html>
<html lang="en">
<head>
<meta charset="utf-8">
<title>Marcus J. Thornbury, RPL – Business Card</title>
<link rel="stylesheet" href="https://fonts.googleapis.com/css2?family=PT+Sans:wght@400&display=swap">
<style>
  :root {
    --page-bg: #ffffff;
    --card-bg: #ffffff;
    --card-border: #000000;
    --navy: #24176b;
    --mark-blue: #0a93e0;
    --mark-outline: #2a1a70;
    --ink: #231f20;
  }
  html, body {
    margin: 0;
    padding: 0;
    width: 1200px;
    height: 1000px;
    overflow: hidden;
    background: var(--page-bg);
    font-family: "PT Sans", "Myriad Pro", Arial, sans-serif;
  }
  .business-card {
    position: absolute;
    left: 75px;
    top: 200px;
    width: 1048px;
    height: 598px;
    border: 1px solid var(--card-border);
    background: var(--card-bg);
  }
  .edge-band {
    position: absolute;
    top: 0;
    right: 0;
    width: 18px;
    height: 100%;
    background: var(--navy);
  }
  .brand-mark {
    position: absolute;
    left: 459px;
    top: 86px;
    width: 132px;
    height: 132px;
  }
  .brand-name {
    position: absolute;
    left: 0;
    width: 1030px;
    top: 232px;
    margin: 0;
    text-align: center;
    font-size: 18px;
    color: var(--navy);
    letter-spacing: 1px;
  }
  .contact-block {
    position: absolute;
    left: 0;
    width: 1050px;
    top: 292px;
    text-align: center;
    color: var(--ink);
  }
  .holder-name {
    margin: 0;
    font-weight: 400;
    font-size: 50px;
    line-height: 66px;
  }
  .holder-name .signature {
    text-decoration: underline;
    text-decoration-color: var(--navy);
    text-decoration-thickness: 2px;
    text-underline-offset: 3px;
    text-decoration-skip-ink: none;
  }
  .contact-line {
    margin: 0;
    font-size: 34px;
    line-height: 52px;
  }
</style>
</head>
<body>
  <div class="business-card">
    <svg class="brand-mark" viewBox="0 0 132 132" aria-hidden="true">
      <circle cx="66" cy="66" r="64" fill="var(--mark-blue)" stroke="var(--mark-outline)" stroke-width="2"/>
    </svg>
    <p class="brand-name">Thornbury Land</p>

    <div class="contact-block">
      <h1 class="holder-name"><span class="signature">Marcus J. Thornbury</span>, RPL</h1>
      <p class="contact-line">Phone: (XXX) XXX-XXXX</p>
      <p class="contact-line">Email: xxxxxxx@mailbox-example.net</p>
    </div>

    <div class="edge-band"></div>
  </div>
</body>
</html>
```